business card and flyer/pricelist

Business Name: Fern Locks Westbrook
new boutique salon run from home, using Australian owned natural products and colours, we need a flyer design to do a letter box drop to advertise the business as well as incorporating a price list on the front (single sided with writing on front and only colour on back)

The salon has a natural feel with light coloured timber chairs, bamboo timber bench top and shelving.

we are after a natural toned colour for the flyer, with possibly a brown/darkish colour writing

we are after a flyer that will also be able to use the design heading (business name) for business cards as well

feel free to look on my pintrest account to get a feel for my style under Marla Quenby.

I love simple clean and Natural looks.

Font styles to use
Script
Other font styles liked:
• SCRIPT HANDWRITTEN FONTS

Colors
cadf82
e9f1ce
5c5c5c
d3d3d3
add136
fee18a

Requirements
Must have
• NATURAL COLOURINGS, eg soft greens, browns,
white or off white background.
Should not have
• photos,

```html
<!DOCTYPE html>
<html lang="en">
<head>
<meta charset="utf-8">
<title>Fern Locks Westbrook – Price List</title>
<link href="https://fonts.googleapis.com/css2?family=Open+Sans:wght@400;600;700&family=Roboto+Condensed:wght@300;700&display=swap" rel="stylesheet">
<style>
  :root {
    --page-bg: #ecebe6;
    --flyer-bg: #e9f1ce;
    --row-light: #f1f5e0;
    --row-dark: #e2eac3;
    --header-bg: #5a5c52;
    --ink: #4a3a28;
    --ink-soft: #5c5c5c;
    --accent: #add136;
    --rule: #b9bfa8;
    --white: #ffffff;
  }
  * { box-sizing: border-box; margin: 0; padding: 0; }
  html, body { width: 1200px; height: 860px; overflow: hidden; }
  body {
    background: var(--page-bg);
    font-family: "Open Sans", Arial, sans-serif;
    position: relative;
  }
  .flyer {
    position: absolute;
    left: 414px; top: 28px;
    width: 372px; height: 804px;
    background: var(--flyer-bg);
    box-shadow: 0 4px 14px rgba(0,0,0,0.12);
  }
  .price-panel {
    position: absolute; left: 0; top: 0;
    width: 306px; height: 804px;
  }
  .brand {
    position: absolute; left: 0; top: 34px; width: 306px;
    text-align: center;
    font-size: 24px; font-weight: 400; letter-spacing: 0.5px;
    color: var(--ink); line-height: 1.2;
  }
  .menu-section {
    position: absolute; left: 29px; width: 248px;
    font-size: 11.5px; color: var(--ink);
  }
  .menu-head {
    display: flex; justify-content: space-between;
    background: var(--header-bg); color: var(--white);
    font-weight: 700; font-size: 11.5px;
    height: 17px; line-height: 17px; padding: 0 9px;
    text-transform: uppercase;
  }
  .menu-row {
    display: flex; justify-content: space-between;
    height: 18px; line-height: 18px; padding: 0 9px;
  }
  .menu-row:nth-child(even) { background: var(--row-light); }
  .menu-row:nth-child(odd) { background: var(--row-dark); }
  .menu-note { padding: 0 9px; line-height: 18px; }
  .cuts { top: 106px; }
  .styling { top: 215px; }
  .colours { top: 360px; }
  .foils { top: 469px; }
  .treatments { top: 598px; }
  .footer-info {
    position: absolute; left: 29px; top: 694px; width: 248px;
    color: var(--ink); font-size: 11px;
  }
  .footer-top {
    display: flex; justify-content: space-between; align-items: center;
    border-top: 1px solid var(--rule); border-bottom: 1px solid var(--rule);
    height: 30px; padding: 0 4px;
  }
  .partner { letter-spacing: 1px; text-transform: uppercase; font-size: 10px; }
  .social { display: flex; align-items: center; gap: 6px; }
  .social-mark { width: 16px; height: 16px; background: var(--ink-soft); }
  .payments {
    display: flex; justify-content: space-between; align-items: center;
    height: 32px; padding: 0 4px; font-weight: 700;
  }
  .payments .divider { width: 1px; height: 16px; background: var(--rule); }
  .badge { width: 28px; height: 16px; border-radius: 50%; border: 1px solid var(--ink-soft); }
  .address-bar {
    position: absolute; left: 0; bottom: 0; width: 306px; height: 25px;
    background: var(--header-bg); color: var(--white);
    font-size: 11px; font-weight: 600; line-height: 25px; padding-left: 14px;
  }
  .offer-strip {
    position: absolute; right: 0; top: 0; width: 66px; height: 804px;
    background: var(--accent);
    display: flex; align-items: center; justify-content: center;
  }
  .offer-text {
    writing-mode: vertical-rl; transform: rotate(180deg);
    font-family: "Roboto Condensed", "Arial Narrow", sans-serif;
    font-size: 23px; color: var(--ink-soft); white-space: nowrap;
    letter-spacing: 0.3px;
  }
  .offer-text strong { font-weight: 700; }
  .offer-text span { font-weight: 300; }
</style>
</head>
<body>
  <main class="flyer">
    <section class="price-panel">
      <h1 class="brand">Fern Locks Westbrook</h1>

      <div class="menu-section cuts">
        <div class="menu-head"><span>Cuts</span><span>Prices</span></div>
        <div>
          <div class="menu-row"><span>Ladies (inc. shampoo/blowdry)</span><span>$45</span></div>
          <div class="menu-row"><span>Mens</span><span>$20</span></div>
          <div class="menu-row"><span>13 &amp; Under</span><span>From $15</span></div>
          <div class="menu-row"><span>5 &amp; Under</span><span>$10</span></div>
        </div>
      </div>

      <div class="menu-section styling">
        <div class="menu-head"><span>Blowdry &amp; Styling</span></div>
        <div>
          <div class="menu-row"><span>Short</span><span>$25</span></div>
          <div class="menu-row"><span>Medium</span><span>$30</span></div>
          <div class="menu-row"><span>Long</span><span>$40</span></div>
          <div class="menu-row"><span>Straight Iron (after blowdry)</span><span>$10</span></div>
          <div class="menu-row"><span>Upstyles</span><span>From $60</span></div>
          <div class="menu-row"><span>Onside styling</span><span>POA</span></div>
        </div>
      </div>

      <div class="menu-section colours">
        <div class="menu-head"><span>Colours</span></div>
        <div>
          <div class="menu-row"><span>Regrowth</span><span>$55</span></div>
          <div class="menu-row"><span>Short</span><span>$60</span></div>
          <div class="menu-row"><span>Medium</span><span>$75</span></div>
          <div class="menu-row"><span>Long</span><span>$85</span></div>
        </div>
      </div>

      <div class="menu-section foils">
        <div class="menu-head"><span>Foils</span></div>
        <div>
          <div class="menu-row"><span>Top Foils</span><span>$50</span></div>
          <div class="menu-row"><span>½ head</span><span>$95</span></div>
          <div class="menu-row"><span>¾ head</span><span>$110</span></div>
          <div class="menu-row"><span>Full head</span><span>$145</span></div>
        </div>
        <p class="menu-note">(all include toner)</p>
      </div>

      <div class="menu-section treatments">
        <div class="menu-head"><span>Treatments</span></div>
        <div>
          <div class="menu-row"><span>At basin</span><span>$10</span></div>
          <div class="menu-row"><span>Special Feel</span><span>$35</span></div>
          <div class="menu-row"><span>Eye brow/lash treatments</span><span>From $10</span></div>
        </div>
      </div>

      <div class="footer-info">
        <div class="footer-top">
          <span class="partner">Kindle Botanics</span>
          <span class="social">Find us on Circlebook <span class="social-mark"></span></span>
        </div>
        <div class="payments">
          <span>Tapcard</span><span class="divider"></span>
          <span>Cardeo</span><span class="divider"></span>
          <span>Payline</span><span class="divider"></span>
          <span class="badge"></span>
        </div>
      </div>

      <div class="address-bar">18 Wattlebark Court Westbrook - 0400 123 987</div>
    </section>

    <aside class="offer-strip">
      <p class="offer-text"><strong>SPECIAL INTRODUCTORY OFFER</strong> <span>-</span> <span>RECEIVE</span> <strong>25% OFF</strong> <span>YOUR INITIAL VISIT</span></p>
    </aside>
  </main>
</body>
</html>
```